Modern, corporate management consultancy firm needs a new website

We need a website for an Australian based management consultancy firm.

The company name is Corbel Strategy Partners.

We are looking for a parallax style wordpress site.

The site needs to provide the following functions:

1) subscribe function
2) links to social media (twitter, linkedin and mail)
3) a gated document section where people can download pdf's from the site after registering or providing name, company, position, email and contact number.

Attached is the company logo, would like to see designs that incorporate the dark blue and silver in the logo and separated into the following sections (Home, About, Services (with 4 options), Our Team, Links, Contacts.

Need the site to be easy to navigate and updated.

Potentially a News Section that can be updated regularly.

Target Market(s)

Target market is SME, business owners and directors

Industry/Entity Type

Management Consulting

Coding

Coded - Design and coding required

Number of Pages Required

1 page

Font styles to use
Sans Serif

Colors
0255a3
cbcbcb
757575
000000

Requirements
Must have
• Must be easy to read and use
Nice to have
• Features are listed on initial brief

```html
<!DOCTYPE html>
<html lang="en">
<head>
<meta charset="utf-8">
<title>Corbel Strategy Partners</title>
<link href="https://fonts.googleapis.com/css2?family=Open+Sans:wght@400;600;700;800&display=swap" rel="stylesheet">
<style>
:root{
  --navy:#1b2b4b;
  --navy-deep:#14213b;
  --blue:#0255a3;
  --silver:#cbcbcb;
  --grey:#757575;
  --light:#f1f1f1;
  --ink:#222;
  --white:#fff;
}
*{margin:0;padding:0;box-sizing:border-box}
html,body{width:1200px;height:2952px;overflow:hidden}
body{font-family:"Open Sans",Arial,sans-serif;color:var(--ink);background:var(--white)}
.wrap{width:1000px;margin:0 auto;position:relative;height:100%}
.section-title{text-align:center;font-weight:700;font-size:22px;letter-spacing:1px;color:var(--ink);text-transform:uppercase}
.rule{width:60px;height:3px;background:var(--navy);margin:12px auto 0}
.btn{display:inline-block;background:var(--navy);color:var(--white);font-size:12px;font-weight:700;letter-spacing:1px;padding:12px 26px;text-transform:uppercase}

/* header */
.site-header{height:132px;border-bottom:1px solid #e4e4e4}
.topbar{position:absolute;right:0;top:10px;font-size:12px;color:var(--grey);display:flex;gap:26px}
.topbar span{display:flex;align-items:center;gap:6px}
.brand{position:absolute;left:0;top:36px;display:flex;align-items:center;gap:14px}
.brand-dot{width:56px;height:56px;border-radius:50%;background:var(--navy)}
.brand-name{font-weight:700;font-size:22px;color:var(--navy);line-height:1.1}
.brand-name small{display:block;font-size:22px}
.main-nav{position:absolute;right:0;top:82px;display:flex;gap:6px}
.main-nav a{font-size:12px;font-weight:600;color:var(--ink);padding:10px 16px;text-decoration:none;letter-spacing:.5px}
.main-nav a.active{background:var(--navy);color:var(--white)}

/* hero */
.hero{height:528px;position:relative;background:linear-gradient(100deg,#c9d1da 0%,#aab6c3 40%,#d6c9b8 75%,#e8e0d4 100%)}
.hero-shade{position:absolute;inset:0;background:linear-gradient(180deg,rgba(20,33,59,.05),rgba(20,33,59,.35))}
.hero-copy{position:absolute;left:0;right:0;top:240px;text-align:center;color:var(--white)}
.hero-copy h1{font-size:44px;font-weight:700;letter-spacing:1px;text-transform:uppercase}
.hero-copy p{font-size:15px;margin-top:14px;line-height:1.6}
.arrow{position:absolute;top:246px;width:36px;height:36px;border-radius:50%;background:rgba(20,33,59,.7);display:flex;align-items:center;justify-content:center}
.arrow.left{left:24px}.arrow.right{right:24px}

/* about */
.about{height:420px;padding-top:56px}
.about-body{display:flex;gap:60px;margin-top:46px}
.about-image{width:400px;height:220px;background:linear-gradient(135deg,#e9e5de,#c8c0b3 60%,#9aa6b5)}
.about-text{flex:1}
.about-text p{font-size:13px;line-height:1.8;color:var(--grey)}
.about-text .btn{margin-top:22px}

/* services */
.services{height:560px;padding-top:20px}
.services .lead{text-align:center;font-size:14px;color:var(--ink);margin-top:18px}
.services .lead b{color:var(--blue)}
.service-band{background:var(--light);height:340px;margin-top:22px}
.service-grid{display:flex;height:100%}
.service{flex:1;text-align:center;padding:38px 20px 0}
.service.featured{background:var(--white);box-shadow:0 0 10px rgba(0,0,0,.12);margin-top:-14px;height:354px;padding-top:52px}
.service-icon{width:84px;height:84px;border-radius:50%;background:var(--white);border:2px solid var(--silver);margin:0 auto;display:flex;align-items:center;justify-content:center}
.service.featured .service-icon{background:var(--navy);border-color:var(--navy)}
.service h3{font-size:14px;font-weight:700;margin-top:22px}
.service p{font-size:11px;line-height:1.7;color:var(--grey);margin-top:12px}
.service .btn{margin-top:22px;padding:10px 22px}
.service .more{display:inline-block;margin-top:24px;font-size:11px;font-weight:700;color:var(--ink)}

/* team */
.team{height:420px;padding-top:12px}
.team-grid{display:flex;gap:20px;margin-top:40px}
.member{flex:1}
.member-photo{height:200px}
.member h4{font-size:15px;font-weight:600;margin-top:16px}
.member p{font-size:11px;line-height:1.6;color:var(--grey);margin-top:6px}
.member a{display:block;font-size:11px;font-weight:700;color:var(--ink);margin-top:8px;text-decoration:none}

/* links */
.other-links{height:320px;background:var(--navy);color:var(--white);padding-top:40px}
.other-links .section-title{color:var(--white)}
.other-links .rule{background:var(--white)}
.other-links .lead{text-align:center;font-size:13px;margin-top:14px;color:var(--silver)}
.badge-row{display:flex;gap:40px;justify-content:center;margin-top:40px}
.badge{width:306px;height:100px;background:var(--white);display:flex;align-items:center;justify-content:center}
.link-arrow{position:absolute;top:172px;width:32px;height:32px;border-radius:50%;background:rgba(255,255,255,.15);display:flex;align-items:center;justify-content:center}

/* news */
.news{height:340px;padding-top:32px}
.news-grid{display:flex;gap:50px;margin-top:46px}
.post{flex:1}
.post h5{font-size:13px;font-weight:700;text-transform:uppercase}
.post time{display:block;font-size:11px;color:var(--grey);margin-top:4px}
.post p{font-size:11px;line-height:1.7;color:var(--grey);margin-top:10px}
.post a{display:block;font-size:11px;font-weight:700;color:var(--ink);margin-top:10px;text-decoration:none}

/* footer */
.site-footer{height:232px;background:var(--navy-deep);color:var(--silver);padding-top:36px}
.footer-grid{display:flex;gap:40px}
.footer-brand{width:300px}
.footer-brand .brand{position:static}
.footer-brand .brand-dot{background:var(--white);width:48px;height:48px}
.footer-brand .brand-name{color:var(--white);font-size:19px}
.footer-brand .brand-name small{font-size:19px}
.footer-brand p{font-size:11px;margin-top:20px}
.footer-col{flex:1}
.footer-col h6{font-size:15px;font-weight:700;color:var(--white);text-transform:uppercase;margin-bottom:14px}
.footer-col li{list-style:none;font-size:11px;line-height:2}
.contact-line{display:flex;gap:8px;font-size:11px;line-height:1.6;margin-bottom:8px}
.newsletter input{display:block;width:100%;height:32px;border:0;background:var(--white);margin-top:10px}
.newsletter .btn{background:var(--blue);margin-top:10px;padding:8px 18px;font-size:11px}
</style>
</head>
<body>

<header class="site-header">
  <div class="wrap">
    <div class="topbar">
      <span><svg width="12" height="12" viewBox="0 0 12 12"><path d="M2 1h2l1 3-1.5 1a7 7 0 0 0 3.5 3.5L8 7l3 1v2a1 1 0 0 1-1 1A9 9 0 0 1 1 2a1 1 0 0 1 1-1z" fill="#757575"/></svg>(02) 9000 4812</span>
      <span><svg width="13" height="10" viewBox="0 0 13 10"><rect x=".5" y=".5" width="12" height="9" fill="none" stroke="#757575"/><path d="M.5.5l6 5 6-5" fill="none" stroke="#757575"/></svg>info@corbelstrategy.com.au</span>
    </div>
    <div class="brand">
      <span class="brand-dot"></span>
      <span class="brand-name">Corbel Strategy<small>Partners</small></span>
    </div>
    <nav class="main-nav">
      <a href="#" class="active" style="background:none;color:var(--ink)">HOME</a>
      <a href="#">ABOUT</a>
      <a href="#">SERVICES</a>
      <a href="#">OUR TEAM</a>
      <a href="#">LINKS</a>
      <a href="#" class="active">CONTACTS</a>
    </nav>
  </div>
</header>

<section class="hero">
  <div role="img" aria-label="Photo of business people in a meeting" style="position:absolute;inset:0"></div>
  <div class="hero-shade"></div>
  <div class="hero-copy">
    <h1>Business Improvement Specialists</h1>
    <p>Helping owners and directors sharpen strategy, lift performance<br>and build businesses that last.</p>
  </div>
  <span class="arrow left"><svg width="12" height="14" viewBox="0 0 12 14"><path d="M9 1L3 7l6 6" fill="none" stroke="#fff" stroke-width="2"/></svg></span>
  <span class="arrow right"><svg width="12" height="14" viewBox="0 0 12 14"><path d="M3 1l6 6-6 6" fill="none" stroke="#fff" stroke-width="2"/></svg></span>
</section>

<section class="about">
  <div class="wrap">
    <h2 class="section-title">About</h2>
    <div class="rule"></div>
    <div class="about-body">
      <div class="about-image" role="img" aria-label="Photo of a planning desk with charts and notes"></div>
      <div class="about-text">
        <p>Corbel Strategy Partners is a boutique management consulting firm that serves SME owners and directors across Australia. We combine practical experience with clear analysis to help businesses find their next step, whether that means growth, restructure or a steady turnaround.</p>
        <p style="margin-top:12px">Our team works alongside you to test ideas, plan change and deliver results that show on the bottom line, with advice that is honest, focused and easy to act on.</p>
        <a class="btn" href="#">Read more</a>
      </div>
    </div>
  </div>
</section>

<section class="services">
  <div class="wrap" style="height:auto">
    <h2 class="section-title">Our Services</h2>
    <div class="rule"></div>
    <p class="lead">Contact us now to learn more and for an obligation free discussion <b>(02) 9000 4812</b> or <b>info@corbelstrategy.com.au</b></p>
  </div>
  <div class="service-band">
    <div class="wrap service-grid">
      <div class="service featured">
        <div class="service-icon"><svg width="36" height="32" viewBox="0 0 36 32"><rect x="2" y="8" width="32" height="22" rx="2" fill="#fff"/><rect x="12" y="2" width="12" height="8" rx="1" fill="none" stroke="#fff" stroke-width="2.5"/><path d="M18 14v10M13 19h10" stroke="#1b2b4b" stroke-width="3"/></svg></div>
        <h3>Business Health Checks</h3>
        <p>A clear review of how your business is tracking, with the strengths, gaps and priorities laid out so you know exactly where to act first.</p>
        <a class="btn" href="#">Read more</a>
      </div>
      <div class="service">
        <div class="service-icon"><svg width="36" height="30" viewBox="0 0 36 30"><rect x="4" y="16" width="6" height="12" fill="#cbcbcb"/><rect x="15" y="9" width="6" height="19" fill="#cbcbcb"/><rect x="26" y="2" width="6" height="26" fill="#cbcbcb"/></svg></div>
        <h3>Business Performance Consulting</h3>
        <p>We find the levers that lift margins, sharpen operations and help your team deliver more with the resources already in place.</p>
        <span class="more">Read more</span>
      </div>
      <div class="service">
        <div class="service-icon"><svg width="34" height="34" viewBox="0 0 34 34"><path d="M27 11A11 11 0 0 0 7 12M7 23a11 11 0 0 0 20-1" fill="none" stroke="#cbcbcb" stroke-width="3"/><path d="M28 4v8h-8M6 30v-8h8" fill="none" stroke="#cbcbcb" stroke-width="3"/></svg></div>
        <h3>Turnaround Management</h3>
        <p>Steady, hands on support when a business is under pressure, from cash flow plans to restructure and a clear path back to health.</p>
        <span class="more">Read more</span>
      </div>
      <div class="service">
        <div class="service-icon"><svg width="30" height="34" viewBox="0 0 30 34"><path d="M15 2l12 5v9c0 8-5 13-12 16C8 29 3 24 3 16V7z" fill="#cbcbcb"/><path d="M9 17l4 4 8-8" fill="none" stroke="#fff" stroke-width="3"/></svg></div>
        <h3>Independent Insolvency Advice</h3>
        <p>Confidential, independent guidance for directors weighing their options, so every decision is informed and made in good time.</p>
        <span class="more">Read more</span>
      </div>
    </div>
  </div>
</section>

<section class="team">
  <div class="wrap">
    <h2 class="section-title">Our Team</h2>
    <div class="rule"></div>
    <div class="team-grid">
      <div class="member">
        <div class="member-photo" role="img" aria-label="Portrait photo of Thomas Reyne" style="background:linear-gradient(135deg,#d8dde3,#9fb0c2)"></div>
        <h4>Thomas Reyne</h4>
        <p>Thomas leads strategy work with owners<br>and boards across many sectors.</p>
        <a href="#">Read Full Bio</a>
      </div>
      <div class="member">
        <div class="member-photo" role="img" aria-label="Portrait photo of Hal Anders" style="background:linear-gradient(135deg,#b8c4d2,#5f7690)"></div>
        <h4>Hal Anders</h4>
        <p>Hal brings deep turnaround experience<br>and a calm approach to hard choices.</p>
        <a href="#">Read Full Bio</a>
      </div>
      <div class="member">
        <div class="member-photo" role="img" aria-label="Portrait photo of Sarah Milne" style="background:linear-gradient(135deg,#eee5d8,#c7a98b)"></div>
        <h4>Sarah Milne</h4>
        <p>Sarah helps teams improve performance<br>with clear systems and measures.</p>
        <a href="#">Read Full Bio</a>
      </div>
    </div>
  </div>
</section>

<section class="other-links">
  <div class="wrap">
    <h2 class="section-title">Other Links</h2>
    <div class="rule"></div>
    <p class="lead">Regulatory and Compliance links</p>
    <div class="badge-row">
      <div class="badge"><svg width="200" height="50"><rect width="200" height="50" rx="4" fill="#e3e3e3"/></svg></div>
      <div class="badge"><svg width="200" height="50"><rect width="200" height="50" rx="4" fill="#e3e3e3"/></svg></div>
      <div class="badge"><svg width="200" height="50"><rect width="200" height="50" rx="4" fill="#e3e3e3"/></svg></div>
    </div>
    <span class="link-arrow" style="left:-70px"><svg width="10" height="14" viewBox="0 0 10 14"><path d="M8 1L2 7l6 6" fill="none" stroke="#fff" stroke-width="2"/></svg></span>
    <span class="link-arrow" style="right:-70px"><svg width="10" height="14" viewBox="0 0 10 14"><path d="M2 1l6 6-6 6" fill="none" stroke="#fff" stroke-width="2"/></svg></span>
  </div>
</section>

<section class="news">
  <div class="wrap">
    <h2 class="section-title">Latest News</h2>
    <div class="rule"></div>
    <div class="news-grid">
      <article class="post">
        <h5>Lorem Ipsum is simply dummy</h5>
        <time>Jun 24 2015</time>
        <p>A short update on planning for the new financial year, with practical steps owners can take now to improve cash flow and reporting.</p>
        <a href="#">Read more</a>
      </article>
      <article class="post">
        <h5>Lorem Ipsum is simply dummy</h5>
        <time>Jun 24 2015</time>
        <p>A short update on planning for the new financial year, with practical steps owners can take now to improve cash flow and reporting.</p>
        <a href="#">Read more</a>
      </article>
      <article class="post">
        <h5>Lorem Ipsum is simply dummy</h5>
        <time>Jun 24 2015</time>
        <p>A short update on planning for the new financial year, with practical steps owners can take now to improve cash flow and reporting.</p>
        <a href="#">Read more</a>
      </article>
    </div>
  </div>
</section>

<footer class="site-footer">
  <div class="wrap footer-grid">
    <div class="footer-brand">
      <div class="brand">
        <span class="brand-dot"></span>
        <span class="brand-name">Corbel Strategy<small>Partners</small></span>
      </div>
      <p>© 2015 Corbel Strategy Partners. All rights reserved.</p>
    </div>
    <div class="footer-col">
      <h6>Quick Link</h6>
      <ul><li>Home</li><li>About</li><li>Services</li><li>Our Team</li><li>Links</li><li>Contacts</li></ul>
    </div>
    <div class="footer-col">
      <h6>Contact</h6>
      <div class="contact-line"><svg width="10" height="14" viewBox="0 0 10 14"><path d="M5 0a5 5 0 0 1 5 5c0 4-5 9-5 9S0 9 0 5a5 5 0 0 1 5-5z" fill="#cbcbcb"/><circle cx="5" cy="5" r="2" fill="#14213b"/></svg><span>Level 9, 41 Harbour Lane,<br>Sydney NSW 2000,<br>Australia</span></div>
      <div class="contact-line"><svg width="12" height="12" viewBox="0 0 12 12"><path d="M2 1h2l1 3-1.5 1a7 7 0 0 0 3.5 3.5L8 7l3 1v2a1 1 0 0 1-1 1A9 9 0 0 1 1 2a1 1 0 0 1 1-1z" fill="#cbcbcb"/></svg><span>(02) 9000 4812</span></div>
      <div class="contact-line"><svg width="13" height="10" viewBox="0 0 13 10"><rect x=".5" y=".5" width="12" height="9" fill="none" stroke="#cbcbcb"/><path d="M.5.5l6 5 6-5" fill="none" stroke="#cbcbcb"/></svg><span>info@corbelstrategy.com.au</span></div>
    </div>
    <div class="footer-col newsletter">
      <h6>Newsletter</h6>
      <p style="font-size:11px">Sign up our newsletter</p>
      <input type="email" aria-label="Email address">
      <a class="btn" href="#">Submit</a>
    </div>
  </div>
</footer>

</body>
</html>
```